Web and Logo Design for eCommerce site

We're launching a sister brand and require a full design for the site.

The site must have an established feel and appeal to corporate and institutional buyers.
Updates

Just a note about the wireframe design:

The Search & Rescue / Coast Guard / NVTB, etc. in the header area aren't buttons or menu items, but rather just info (along the lines of a tagline).  Sort of a "who we serve" sort of thing.

Worth noting is that it's specifically geared towards LARGE BUYERS.  For example, a police force buying 200 headlamps and 85 pairs of gloves.  So they'll register + sign in and then add a bunch of items to a RFQ.

Aim for a professional, masculine design.

Target Market(s)

We will be selling outdoor gear to the military, law enforcement, fire and rescue and first responders.

Requirements
Must have
• We require:
- Logo (vector based)

Site:
- template page
* main site template, re-skinned version of our current site
* horizontal drop-down menu
- product listings page
* thumbnail view of products
- product details page
* including elements such as product image, color/size selector, descriptions and specs (again, based loosely on our current website)
- account management page
* illustrating basic data entry styles for text box, buttons, grid, etc.

The site needs to be given a responsive design, so 2 versions of each design should be presented for desktop + mobile views.

Additional funds are available if the designer is able to fully implement the designs into a responsive framework such as bootstrap.

Nice to have
• Clean, professional design similar to:

http://military.brambletrekgear.com/gov/accessories/gloves.html

http://leaf.quenvolt.com/ProductFind.aspx?language=EN&category=Hardshell&subcat=Waterproof_Jackets

```html
<!DOCTYPE html>
<html lang="en">
<head>
<meta charset="utf-8">
<title>Kestrel – Outdoor Gear for First Responders</title>
<link href="https://fonts.googleapis.com/css2?family=Open+Sans:ital,wght@0,300;0,400;0,600;0,700;1,300;1,400&display=swap" rel="stylesheet">
<style>
:root{
  --ink:#111;
  --header:#0c0c0c;
  --band:#e6e6e6;
  --white:#fff;
  --nav:#2c2c2c;
  --nav-active:#1c1c1c;
  --nav-text:#e6e6e6;
  --red:#b0161c;
  --modal-red:#c0161c;
  --grey-text:#555;
  --side:#efefef;
  --card-border:#d6d6d6;
  --footer:#1a1a1a;
  --footer-text:#cfcfcf;
  --dark-btn:#333;
  --veil:rgba(0,0,0,.64);
}
*{box-sizing:border-box;margin:0;padding:0}
html,body{width:822px;height:1200px;overflow:hidden}
body{position:relative;font-family:"Open Sans",Arial,sans-serif;background:var(--white);color:var(--ink)}
.abs{position:absolute}

.site-header{left:0;top:0;width:822px;height:93px;background:linear-gradient(#1a1a1a,var(--header))}
.brand{left:70px;top:20px;color:#e8e8e8}
.brand-name{display:flex;align-items:center;gap:8px;font-size:30px;font-weight:600;line-height:36px}
.brand-name i{display:block;width:14px;height:14px;background:#e8e8e8}
.brand-sub{margin-top:3px;font-size:8px;letter-spacing:1.5px;border:1px solid #aaa;padding:1px 5px;width:174px;text-transform:uppercase}
.tagline{right:70px;top:28px;text-align:right;font-size:13px;font-style:italic;font-weight:300;color:#bbb;line-height:19px}

.login-band{left:0;top:93px;width:822px;height:42px;background:var(--band)}
.login-label{left:200px;top:106px;font-size:13px;color:#222}
.lock{left:178px;top:105px}
.field{background:var(--white);border:1px solid #ccc;font-size:9px;color:#999;padding:3px 8px;height:21px}
.btn-login{left:596px;top:104px;width:47px;height:21px;background:#2b2b2b;color:#eee;font-size:9.5px;text-align:center;line-height:21px}

.serve-band{left:0;top:135px;width:822px;height:40px;background:var(--white);display:flex;justify-content:center;align-items:center;gap:10px;font-size:13px;color:var(--red)}
.serve-band span.sep{color:#aaa}

.main-nav{left:0;top:175px;width:822px;height:36px;background:var(--nav);display:flex;padding-left:70px}
.main-nav a{color:var(--nav-text);font-size:9.8px;line-height:36px;padding:0 13px;text-decoration:none;text-transform:uppercase}
.main-nav a.active{background:var(--nav-active)}

.hero{left:68px;top:220px;width:686px;height:260px;background:linear-gradient(180deg,#5d7ea6 0%,#a9bdd2 45%,#d9e0e6 70%,#6c6f73 100%)}
.hero-caption{left:85px;top:241px;width:151px;height:218px;background:rgba(20,20,20,.82);padding:26px 10px 0 11px;color:#eee;overflow:hidden}
.hero-caption h2{font-size:13px;font-weight:700;line-height:19px;white-space:nowrap}
.hero-caption p{margin-top:9px;font-size:9px;line-height:17px;white-space:nowrap}
.dots{display:flex;gap:6px;margin-top:20px}
.dots i{width:7px;height:7px;border-radius:50%;background:#ddd}

.sidebar-head{left:68px;top:501px;width:164px;height:28px;background:#3b3b3b;color:#eee;font-size:13px;line-height:28px;padding-left:10px}
.category-list{left:68px;top:529px;width:164px;height:266px;background:var(--side);list-style:none;padding-top:14px}
.category-list li{font-size:9.8px;color:#555;height:31.5px;padding-left:9px}
.category-list li b{color:#999;font-weight:400;margin-right:8px}
.offer{left:68px;top:805px;width:164px;height:160px;background:var(--side)}
.offer h3{position:absolute;left:10px;top:20px;font-size:12.5px;font-weight:400;color:#444}
.offer-photo{left:12px;top:47px;width:90px;height:92px;background:radial-gradient(ellipse at 50% 55%,#6b4330 0%,#4a2d20 55%,#efefef 72%)}
.offer-pct{left:104px;top:45px;color:var(--red);font-size:25px;line-height:26px}
.offer-word{left:104px;top:72px;color:var(--red);font-size:16px}

.section-title{left:247px;top:505px;font-size:13px;font-weight:600;color:#444}
.card{width:156px;height:179px;border:1px solid var(--card-border);background:#fafafa;text-align:center}
.card .pic{position:absolute;left:50%;top:25px;transform:translateX(-50%)}
.card .name{position:absolute;left:0;right:0;top:120px;font-size:9.8px;font-weight:600;color:#333}
.card .price{position:absolute;left:0;right:0;top:136px;font-size:9.8px;color:var(--red)}
.card svg.basket{position:absolute;left:70px;top:155px}

.sort-row{left:248px;top:938px;font-size:9.8px;color:#555;display:flex;gap:8px}
.sort-row u{color:#222}
.pager{top:938px;width:16px;height:16px;border-radius:50%;background:#ccc}

.site-footer{left:0;top:986px;width:822px;height:214px;background:var(--footer);color:var(--footer-text)}
.f-col{position:absolute;top:18px}
.f-col h4{font-size:12px;font-weight:400;color:#ddd;margin-bottom:9px}
.f-col a{display:block;font-size:9px;line-height:17px;color:#bbb;text-decoration:none}
.f-col p{font-size:9px;line-height:13px;color:#888;width:170px}
.f-input{width:168px;height:19px;background:#eee;border:1px solid #999;color:#555;font-size:8.5px;padding:2px 10px;margin-top:5px}
.subscribe{position:absolute;left:104px;top:108px;width:65px;height:19px;background:#3a3a3a;color:#ddd;font-size:9.5px;text-align:center;line-height:19px}
.social a{display:flex;align-items:center;gap:8px;line-height:22px}
.social a i{width:17px;height:17px;border-radius:50%;background:#e0e0e0;display:block}
.copyright{left:0;top:1174px;width:822px;text-align:center;font-size:8.5px;color:#777}

.veil{left:0;top:0;width:822px;height:1200px;background:var(--veil)}
.modal{left:209px;top:262px;width:404px;height:176px;background:var(--white);text-align:center;box-shadow:0 0 10px rgba(0,0,0,.5)}
.modal p{position:absolute;left:0;right:0;top:19px;font-size:12.6px;line-height:20px;color:var(--modal-red);text-transform:uppercase}
.modal .email{position:absolute;left:57px;top:131px;width:207px;height:26px;border:1px solid #ccc;background:#fafafa;text-align:left;font-size:9px;color:#777;padding:6px 10px}
.modal .register{position:absolute;left:270px;top:131px;width:72px;height:26px;background:var(--dark-btn);color:#eee;font-size:11.5px;line-height:26px}
.close{left:599px;top:254px}
</style>
</head>
<body>

<header class="abs site-header"></header>
<div class="abs brand">
  <div class="brand-name"><i></i>Kestrel</div>
  <div class="brand-sub">Kestrel Field Pro Supply</div>
</div>
<div class="abs tagline">“ Great Outdoor Gear for<br>Canada’s First Responders”</div>

<div class="abs login-band"></div>
<svg class="abs lock" width="14" height="18" viewBox="0 0 14 18"><path d="M3 8V5a4 4 0 0 1 8 0v3" fill="none" stroke="#222" stroke-width="2"/><rect x="0" y="8" width="14" height="10" rx="1" fill="#222"/></svg>
<div class="abs login-label">CUSTOMER LOGIN</div>
<div class="abs field" style="left:323px;top:104px;width:132px">Username</div>
<div class="abs field" style="left:461px;top:104px;width:132px">Password</div>
<div class="abs btn-login">LOGIN</div>

<div class="abs serve-band">
  <span>SEARCH AND RESCUE</span><span class="sep">/</span><span>COAST GUARD</span><span class="sep">/</span><span>NVTB</span><span class="sep">/</span><span>FIRE</span><span class="sep">/</span><span>MILITARY</span><span class="sep">/</span><span>LAW ENFORCEMENT</span>
</div>

<nav class="abs main-nav">
  <a class="active" href="#">Rescue Gear</a><a href="#">Footwear</a><a href="#">Clothing</a><a href="#">Tents, Mats, Sleeping Bags</a><a href="#">Camping Gear</a><a href="#">Snow Sports</a><a href="#">Brands</a>
</nav>

<div class="abs hero" role="img" aria-label="Climber with ice axe on a snowy mountain ridge under a blue sky"></div>
<div class="abs hero-caption">
  <h2>AENEAN NON ODIO<br>EGESTAS, LAOREET<br>NUNC EGET</h2>
  <p>Sed accumsan auctor diam<br>malesuada convallis libero<br>egestas non. Sed ut venen<br>metus. Aliquam erat volut<br>Nunc et mi quis lacus.</p>
  <div class="dots"><i></i><i></i><i></i><i></i><i></i></div>
</div>

<div class="abs sidebar-head">PRODUCT CATEGORY</div>
<ul class="abs category-list">
  <li><b>&gt;|</b>Vivamus pulvinar</li>
  <li><b>&gt;|</b>Consectetr adipiscing</li>
  <li><b>&gt;|</b>Mauris iddui necnunc</li>
  <li><b>&gt;|</b>Nunc convallis enim</li>
  <li><b>&gt;|</b>Nulla faucibusNullam</li>
  <li><b>&gt;|</b>Nisl egetio vitae</li>
  <li><b>&gt;|</b>Suspendisse consect</li>
  <li><b>&gt;|</b>Aliquam ullamcorpe</li>
</ul>
<div class="abs offer">
  <h3>PRODUCT OFFER</h3>
  <div class="abs offer-photo" role="img" aria-label="Pair of brown leather hiking boots"></div>
  <div class="abs offer-pct">30%</div>
  <div class="abs offer-word">OFFER</div>
</div>

<div class="abs section-title">LATEST PRODUCTS</div>

<div class="abs card" style="left:247px;top:531px"><div class="pic" role="img" aria-label="Red hardshell jacket" style="width:50px;height:72px;background:#c2301f;border-radius:12px 12px 4px 4px"></div><div class="name">Phasellus quis mauris</div><div class="price">Price : $00.00</div><svg class="basket" width="16" height="13" viewBox="0 0 16 13"><path d="M4 5 7 0M12 5 9 0" stroke="#333" stroke-width="1.5"/><path d="M0 4h16v2h-1l-2 7H3L1 6H0z" fill="#333"/></svg></div>
<div class="abs card" style="left:422px;top:531px"><div class="pic" role="img" aria-label="Green avalanche beacon" style="width:26px;height:50px;top:32px;background:linear-gradient(#666 40%,#4caf3a 40%);border-radius:4px"></div><div class="name">Phasellus quis mauris</div><div class="price">Price : $00.00</div><svg class="basket" width="16" height="13" viewBox="0 0 16 13"><path d="M4 5 7 0M12 5 9 0" stroke="#333" stroke-width="1.5"/><path d="M0 4h16v2h-1l-2 7H3L1 6H0z" fill="#333"/></svg></div>
<div class="abs card" style="left:596px;top:531px"><div class="pic" role="img" aria-label="Pair of patterned skis" style="width:28px;height:72px;background:repeating-linear-gradient(90deg,#2a6a6a 0 7px,#c14a2a 7px 10px,#fafafa 10px 12px)"></div><div class="name">Phasellus quis mauris</div><div class="price">Price : $00.00</div><svg class="basket" width="16" height="13" viewBox="0 0 16 13"><path d="M4 5 7 0M12 5 9 0" stroke="#333" stroke-width="1.5"/><path d="M0 4h16v2h-1l-2 7H3L1 6H0z" fill="#333"/></svg></div>

<div class="abs card" style="left:247px;top:732px"><div class="pic" role="img" aria-label="Orange climbing harness" style="width:44px;height:66px;background:#b0653a;border-radius:10px"></div><div class="name">Phasellus quis mauris</div><div class="price">Price : $00.00</div><svg class="basket" width="16" height="13" viewBox="0 0 16 13"><path d="M4 5 7 0M12 5 9 0" stroke="#333" stroke-width="1.5"/><path d="M0 4h16v2h-1l-2 7H3L1 6H0z" fill="#333"/></svg></div>
<div class="abs card" style="left:422px;top:732px"><div class="pic" role="img" aria-label="Green and black ski binding" style="width:52px;height:22px;top:46px;background:linear-gradient(90deg,#2f8a3a,#222);border-radius:6px"></div><div class="name">Phasellus quis mauris</div><div class="price">Price : $00.00</div><svg class="basket" width="16" height="13" viewBox="0 0 16 13"><path d="M4 5 7 0M12 5 9 0" stroke="#333" stroke-width="1.5"/><path d="M0 4h16v2h-1l-2 7H3L1 6H0z" fill="#333"/></svg></div>
<div class="abs card" style="left:596px;top:732px"><div class="pic" role="img" aria-label="Blue and white ski boot" style="width:54px;height:70px;background:linear-gradient(#e8eef2 30%,#3f9ec0 30%);border-radius:8px"></div><div class="name">Phasellus quis mauris</div><div class="price">Price : $00.00</div><svg class="basket" width="16" height="13" viewBox="0 0 16 13"><path d="M4 5 7 0M12 5 9 0" stroke="#333" stroke-width="1.5"/><path d="M0 4h16v2h-1l-2 7H3L1 6H0z" fill="#333"/></svg></div>

<div class="abs sort-row"><span>SORT BY :</span><u>DEFAULT</u><span style="color:#aaa">/</span><span>PRICE</span><span style="color:#aaa">/</span><span>NAME</span></div>
<div class="abs pager" style="left:713px"></div>
<div class="abs pager" style="left:734px"></div>

<footer class="abs site-footer">
  <div class="f-col" style="left:70px"><h4>Quick Links</h4><a>Home</a><a>Rescue Gear</a><a>Footwear</a><a>Clothing</a><a>Tents, Mats, Sleeping Bags</a><a>Camping Gear</a><a>Snow Sports</a></div>
  <div class="f-col" style="left:226px"><h4>Products For</h4><a>Search and Rescue</a><a>Coast Guard</a><a>NVTB</a><a>Fire</a><a>Military</a><a>Law Enforcement</a><a>Brands</a></div>
  <div class="f-col" style="left:347px"><h4>Support Links</h4><a>Press</a><a>Legal Notice</a><a>Privacy Policy</a><a>Term of Use</a></div>
  <div class="f-col" style="left:457px"><h4>Newsletters Sign Up</h4><p>Sign up for our daily email by entering your information below</p><div class="f-input">Your name</div><div class="f-input">Email address</div><div class="subscribe">SUBSCRIBE</div></div>
  <div class="f-col social" style="left:665px"><h4>Connect With Us</h4><a><i></i>Circlebook</a><a><i></i>Chirpline</a><a><i></i>WorkNet</a></div>
</footer>
<div class="abs copyright">Copyright © 2014 &nbsp;Kestrel. &nbsp;All rights reserved.</div>

<div class="abs veil"></div>
<div class="abs modal">
  <p>Please register to enter and enjoy<br>Canada’s best selection of outdoor gear at special<br>pricing and terms that refelect your commitment<br>to service and duty, your unique position<br>and credentials</p>
  <div class="email">Enter your email ID</div>
  <div class="register">REGISTER</div>
</div>
<svg class="abs close" width="22" height="22" viewBox="0 0 22 22"><circle cx="11" cy="11" r="10" fill="#444" stroke="#fff" stroke-width="2"/><path d="M7.5 7.5l7 7M14.5 7.5l-7 7" stroke="#fff" stroke-width="2"/></svg>

</body>
</html>
```